Geschäftspapiere für Rechnungen, Anschreiben etc.
Zielgruppe
Yogaunterricht - Einzelstunden, Workshops, Seminare etc.
Aufgabenstellung
Es soll weiche Übergänge haben mit dem bestehenden Logo und gerne den Farbverlauf nutzen. Auf das Briefpapier muss der Name, die Adresse, Web- und Emailadresse: www.velin-yoga.com

```html
<!DOCTYPE html>
<html lang="de">
<head>
<meta charset="utf-8">
<title>Velin Yoga – Briefpapier</title>
<link rel="stylesheet" href="https://fonts.googleapis.com/css2?family=Arimo:wght@400;700&family=Gudea:wght@400&display=swap">
<style>
  :root {
    --backdrop: #ecebe8;
    --paper: #ffffff;
    --band-top: #4b7a2c;
    --band-bottom: #2c3b3a;
    --ornament: rgba(255,255,255,0.08);
    --ink: #111111;
    --muted: #8a8a8a;
    --subject: #a3a3a3;
    --rule: #c9c9c9;
    --brand-ring: #9fcf8f;
  }
  * { margin: 0; padding: 0; box-sizing: border-box; }
  html, body { width: 1061px; height: 1200px; overflow: hidden; background: var(--backdrop); }
  .letterhead {
    position: absolute; left: 127px; top: 30px;
    width: 806px; height: 1140px;
    background: var(--paper);
    box-shadow: 0 2px 10px rgba(0,0,0,0.12);
    font-family: "Arimo", Arial, sans-serif;
    color: var(--ink);
  }
  .side-band {
    position: absolute; right: 0; top: 0; width: 30px; height: 100%;
    background: linear-gradient(to bottom, var(--band-top) 0%, #3f5f30 45%, var(--band-bottom) 100%);
  }
  .side-band-ornament {
    position: absolute; right: 0; bottom: 0; width: 30px; height: 300px;
    background: linear-gradient(to bottom, transparent, var(--ornament));
  }
  .brand {
    position: absolute; right: 62px; top: 22px; width: 200px; text-align: center;
    font-family: "Gudea", Arial, sans-serif; color: var(--muted);
  }
  .brand-circle {
    width: 74px; height: 74px; border-radius: 50%;
    border: 2px solid var(--brand-ring); margin: 0 auto 10px;
  }
  .brand-name { font-size: 26px; letter-spacing: 2px; text-transform: uppercase; }
  .contact {
    position: absolute; right: 56px; top: 158px;
    font-family: "Gudea", Arial, sans-serif; font-size: 14px; color: var(--muted);
    text-align: right; line-height: 17px;
  }
  .contact-row { display: flex; justify-content: flex-end; align-items: center; gap: 8px; margin-bottom: 8px; }
  .contact-icon { width: 24px; height: 24px; flex: none; }
  .sender-line {
    position: absolute; left: 90px; top: 176px; width: 330px;
    font-size: 8px; color: var(--muted);
    border-bottom: 1px solid var(--rule); padding-bottom: 3px;
  }
  .recipient { position: absolute; left: 96px; top: 224px; font-size: 13px; line-height: 16px; }
  .recipient .city { margin-top: 16px; }
  .subject { position: absolute; left: 110px; top: 356px; font-size: 19px; font-weight: 700; color: var(--subject); }
  .salutation { position: absolute; left: 116px; top: 430px; font-size: 15px; }
  .body-text { position: absolute; left: 120px; top: 490px; font-size: 15px; line-height: 27px; }
  .fold-mark { position: absolute; left: 0; width: 26px; border-top: 1px solid var(--rule); }
</style>
</head>
<body>
<main class="letterhead">
  <div class="side-band"></div>
  <div class="side-band-ornament" role="img" aria-label="Dezentes florales Ornament im Farbband"></div>

  <header class="brand">
    <div class="brand-circle"></div>
    <div class="brand-name">Velin Yoga</div>
  </header>

  <address class="contact" style="font-style:normal">
    <div class="contact-row">
      <span>Mira Holmbach<br>Lindenweg 24<br>35037 Talheim</span>
      <svg class="contact-icon" viewBox="0 0 24 24"><circle cx="12" cy="12" r="11" fill="none" stroke="#8a8a8a" stroke-width="1.4"/><rect x="6.5" y="8" width="11" height="8" fill="none" stroke="#8a8a8a" stroke-width="1.3"/><path d="M6.5 8 L12 12.5 L17.5 8" fill="none" stroke="#8a8a8a" stroke-width="1.3"/></svg>
    </div>
    <div class="contact-row">
      <span>Tel.: 0151/2046618</span>
      <svg class="contact-icon" viewBox="0 0 24 24"><circle cx="12" cy="12" r="11" fill="none" stroke="#8a8a8a" stroke-width="1.4"/><path d="M8.5 6.5 L10.5 9.5 L9.2 10.8 C10 12.6 11.4 14 13.2 14.8 L14.5 13.5 L17.5 15.5 L16 17.5 C11 17 7 13 6.5 8 Z" fill="none" stroke="#8a8a8a" stroke-width="1.3" stroke-linejoin="round"/></svg>
    </div>
    <div class="contact-row">
      <span>mail@velin-yoga.com<br>www.velin-yoga.com</span>
      <svg class="contact-icon" viewBox="0 0 24 24"><circle cx="12" cy="12" r="11" fill="none" stroke="#8a8a8a" stroke-width="1.4"/><text x="12" y="16.5" text-anchor="middle" font-family="Arial, sans-serif" font-size="13" fill="#8a8a8a">@</text></svg>
    </div>
  </address>

  <div class="sender-line">Velin Yoga • Mira Holmbach • Lindenweg 24 • 35037 Talheim</div>

  <div class="recipient">
    Frau<br>Vorname Nachname<br>Musterstrasse 9
    <div class="city">99999 Musterort</div>
  </div>

  <h1 class="subject">Hier steht der Betreff</h1>
  <p class="salutation">Sehr geehrte Frau Musterfrau,</p>
  <p class="body-text">[Inhalt]<br>[Inhalt]<br>[Inhalt]<br>[Inhalt]<br>[Inhalt]<br>[Inhalt]<br>[Inhalt]</p>

  <div class="fold-mark" style="top:400px"></div>
  <div class="fold-mark" style="top:540px"></div>
  <div class="fold-mark" style="top:730px"></div>
</main>
</body>
</html>
```